NOTE: I PROVIDED THE INCORRECT LOGO AND ONLY A HANDFUL OF PEOPLE NOTICED THAT IT WAS NOT THE ONE I DESCRIBED. THE LOGO I HAVE NOW ATTACHED MATCHES MY WEBSITE AND THE COLORS ON THE WEBSITE SHOULD BE USED FOR THE CARD.

PLEASE READ THE BUSINESS CARD DETAILS AND PROJECT MUST HAVES CAREFULLY.

I am looking for a business card that is powerful, a bit edgy, and although I work in the corporate world, not too formal. I would like to see designs that use the colors on my website www.brightlumo.com. I don't want the card to look washed out so please use shades of those colors that make them "pop". The "vibe" of the card needs to show substance and confidence while also reflecting that we're not your usual consultants.

The focus of my work is turning "people problems" into profits. Those problems could be poor service, an unstable workforce, untrained leaders, or managing change. We are an aggressive, results-focused team of performance improvement professionals who refuse to believe "things can't be done". For us, failure is not an option. Our logo reflects a target from the view of the site on a gun.

In addition to the contact information provided on the sample business card (do not include "turning people problems into profits"), I would like to include this statement (probably on the back):
I equip results-oriented business leaders to turn their people problems into profits in six months or less.

PLEASE NOTE THAT MY WEBSITE IS UNDER REVISION TO TONE DOWN THE MILITARY THEME, ALTHOUGH THE WARRIOR ENERGY AND FOCUS ON RESULTS REMAINS.

Target Market(s)

My clients are Mid and senior-level managers. I don't target any particular industry.

Industry/Entity Type

Consulting

Contact Information for Business Card

In addition to the contact information provided on the sample business card (DO NOT INCLUDE "turning people problems into profits"), I would like to include this statement (probably on the back):

I don't care whether the card is landscape or portrait view.

Font styles to use
Sans Serif

Requirements
Must have
• 1. be easy to read, no 6-8 point fonts!
• 2. a "vibe" that captures the eye without being too chaotic or busy
• 3. bold color, not washed out or boring - a good blend with the colors currently on my website (black, red, white, army green) but you don't need to use all of them.
• 4. all the contact information I have provided
• 5. a good blend with the colors currently on my website
• 6. Must have this quote on the back of the card: I equip results-oriented business leaders to turn their people problems into profits in six months or less.
Nice to have
• In looking at the sample images I provided for ideas, you can see that I like the way a card carries over from one side to the next.
• It would be great to find some aspect/quality/feature that I haven't seen before
Should not have
• 1. NO use of ALL CAPS
• 2. fonts that I would have to seek out and purchase (you should provide files for font if using something not standard)

```html
<!DOCTYPE html>
<html lang="en">
<head>
<meta charset="utf-8">
<title>Brightlumo Partners — Business Card</title>
<link href="https://fonts.googleapis.com/css2?family=Montserrat:wght@400;500;700&display=swap" rel="stylesheet">
<style>
  :root {
    --stage: #8f8f8f;
    --card: #141414;
    --army: #7a9a32;
    --red: #d62828;
    --white: #ffffff;
    --soft-white: #e6e6e6;
  }
  * { box-sizing: border-box; margin: 0; padding: 0; }
  html, body { width: 1200px; height: 1200px; overflow: hidden; }
  body {
    background: var(--stage);
    font-family: "Montserrat", sans-serif;
    position: relative;
  }
  .card {
    position: absolute;
    left: 180px;
    width: 840px;
    height: 480px;
    background: var(--card);
    overflow: hidden;
  }
  .card--front { top: 90px; }
  .card--back { top: 630px; }

  .wordmark {
    position: absolute;
    display: flex;
    align-items: center;
    gap: 14px;
    color: var(--army);
    font-weight: 500;
    letter-spacing: -0.5px;
    white-space: nowrap;
  }
  .wordmark__square {
    width: 22px; height: 22px;
    background: var(--red);
    flex: none;
  }
  .card--front .wordmark { left: 200px; top: 150px; font-size: 46px; }
  .card--back .wordmark { left: 60px; top: 222px; font-size: 32px; gap: 10px; }
  .card--back .wordmark__square { width: 16px; height: 16px; }

  .statement {
    position: absolute;
    left: 200px;
    top: 238px;
    width: 520px;
    color: var(--soft-white);
    font-size: 19px;
    font-weight: 400;
    line-height: 1.5;
  }
  .statement strong { color: var(--red); font-weight: 700; }

  .accent-bar {
    position: absolute;
    height: 16px;
    background: var(--army);
  }
  .card--front .accent-bar { left: 320px; right: 110px; bottom: 60px; }
  .card--back .accent-bar { left: 390px; right: 60px; bottom: 62px; }

  .contact {
    position: absolute;
    left: 470px;
    top: 92px;
    color: var(--white);
  }
  .contact__name { font-size: 31px; font-weight: 700; letter-spacing: 0.2px; }
  .contact__title { font-size: 17px; color: var(--red); font-weight: 500; margin-top: 2px; }
  .contact__list { list-style: none; margin-top: 28px; }
  .contact__item {
    display: flex; align-items: center; gap: 12px;
    font-size: 20px; line-height: 32px;
  }
  .contact__item svg {
    width: 20px; height: 20px; flex: none;
    stroke: var(--army); fill: none; stroke-width: 1.6;
    stroke-linecap: round; stroke-linejoin: round;
  }
</style>
</head>
<body>
  <section class="card card--front" aria-label="Card front">
    <div class="wordmark"><span class="wordmark__square"></span>Brightlumo Partners</div>
    <p class="statement">I equip results-oriented business leaders to turn their people problems into profits <strong>in six months or less.</strong></p>
    <div class="accent-bar"></div>
  </section>

  <section class="card card--back" aria-label="Card back">
    <div class="wordmark"><span class="wordmark__square"></span>Brightlumo Partners</div>
    <div class="contact">
      <p class="contact__name">Dana Whitfield</p>
      <p class="contact__title">Chief Performance Strategist</p>
      <ul class="contact__list">
        <li class="contact__item">
          <svg viewBox="0 0 20 20"><rect x="5" y="1.5" width="10" height="17" rx="1.5"/><line x1="8.5" y1="15.5" x2="11.5" y2="15.5"/></svg>
          248-555-0142
        </li>
        <li class="contact__item">
          <svg viewBox="0 0 20 20"><path d="M4 2.5l3 0.5 1.2 3.5-2 1.5a10 10 0 0 0 5.8 5.8l1.5-2 3.5 1.2 0.5 3c-0.5 1-1.5 1.5-2.5 1.5C8 17.5 2.5 12 2.5 5c0-1 0.5-2 1.5-2.5z"/></svg>
          248-555-0187
        </li>
        <li class="contact__item">
          <svg viewBox="0 0 20 20"><rect x="2" y="4.5" width="16" height="11" rx="1"/><polyline points="2.5,5 10,11 17.5,5"/></svg>
          danaw@brightlumo.com
        </li>
        <li class="contact__item">
          <svg viewBox="0 0 20 20"><polyline points="2,10 10,3 18,10"/><polyline points="4.5,8 4.5,17 15.5,17 15.5,8"/><rect x="8.5" y="12" width="3" height="5"/></svg>
          www.brightlumo.com
        </li>
      </ul>
    </div>
    <div class="accent-bar"></div>
  </section>
</body>
</html>
```